Luxury Green Court Club/academy - Webdesign

We want to develop a cutting edge website for a luxury tennis academy. Academy is based in Russia and includes all the necessary amenities for comfortable stay: apartments, spa, tennis courts, training facilities, etc.
We would like to see a clean, simple and modern design (with implementation of all the current trends in web design, although our project has to be distinct and unique).
Color scheme: we would like to see colors present in our logos and all the current associated with tennis. We are open to your ideas and creativity on this front.
The final design should communicate simplicity, be user friendly and convey premium feel.
We woud like to see unique ideas in the design, unconventional techniques, etc.
We don't want standard template design!
Updates
We want to mention that this Tennis Academy has a light focus on nature, as the new material we have uploaded illustrates.
Additional comment to everyone!
We couldn't upload this file to the system: it is too big.
Thank you everyone for your submissions!
Industry/Entity Type
Training
Requirements
Must have
- We would like to see the designs for the following pages:
Home Page:
- Slideshow
- Short description and all the standard stuff
About Us:
- Description with some images
Services:
- Simple description of all of the provided services and possibility to book all of them on the website
! Important ! Develop small system for booking of the days of stay and registration for the courses
Booking and registration !
News:
- Creative layout to display recent news of the academy
Coaches:
- Image and short description of our staff.
Club / Gallery:
- Images and descriptions of the amenities in the territory.
We want a unique display of images: not just lines and rows filled with images
- One idea: an interactive map that displays images and description on mouseover or click on the object on the map (but again, we are open to all your ideas)
Contacts:
- Contact form, contacts, etc.
Sport Store:
- Basic layout for the goods and services provided by the sports store located in the academy
Prices:
- Price lists and ranges with a button leading to registration and booking
For pages like About Us and Services, it would be enough to develop one unified layout for all of them.

```html
<!DOCTYPE html>
<html lang="en">
<head>
<meta charset="utf-8">
<title>Green Court Club</title>
<link href="https://fonts.googleapis.com/css2?family=Ubuntu:wght@300;400;500;700&family=Yanone+Kaffeesatz:wght@300;400&family=Arimo:wght@400&display=swap" rel="stylesheet">
<style>
:root{
  --green:#2f9a24;
  --green-dark:#217a17;
  --green-text:#3bb32c;
  --bg:#232425;
  --nav-text:#d6d6d6;
  --body-text:#c9c9c9;
  --white:#ffffff;
}
*{box-sizing:border-box;margin:0;padding:0}
html,body{width:1004px;height:1200px;overflow:hidden}
body{background:var(--bg);font-family:'Ubuntu',sans-serif;color:var(--body-text);position:relative}
.top-strip{position:absolute;left:0;top:0;width:1004px;height:6px;background:#1b1c1d}
.header{position:absolute;left:0;top:6px;width:1004px;height:100px;background:var(--green);box-shadow:0 2px 4px rgba(0,0,0,.4)}
.brand{position:absolute;left:152px;top:30px;display:flex;align-items:center;gap:8px;font-weight:700;font-size:22px;color:var(--white)}
.brand-dot{width:18px;height:18px;border-radius:50%;background:var(--white)}
.phones{position:absolute;left:744px;top:14px;font-family:'Arimo',sans-serif;font-size:14px;color:var(--white)}
.phones div{display:flex;align-items:center;gap:10px;height:22px}
.search{position:absolute;left:715px;top:65px;width:139px;height:20px;background:var(--green-dark);border:1px solid #2a8a20;font-family:'Arimo',sans-serif;font-style:italic;font-size:8px;color:#1c5a14;padding:5px 8px}
.search svg{position:absolute;right:5px;top:4px}
.nav{position:absolute;left:150px;top:106px;width:704px;height:36px;display:flex;border-bottom:1px solid #2e2f30}
.nav a{flex:1;text-align:center;font-family:'Yanone Kaffeesatz',sans-serif;font-weight:300;font-size:16px;color:var(--nav-text);text-decoration:none;line-height:36px;border-left:1px solid #3a3b3c;white-space:nowrap}
.nav a:last-child{border-right:1px solid #3a3b3c}
.nav a.active span{background:var(--green);color:var(--white);padding:1px 6px;font-weight:400}
.hero{position:absolute;left:151px;top:165px;width:702px;height:303px;border:1px solid #555;background:linear-gradient(180deg,#5d8a3a 0%,#7fa24a 45%,#b47a52 70%,#c08a66 100%)}
.hero h1{position:absolute;left:24px;top:66px;width:380px;font-family:'Arimo',sans-serif;font-weight:400;font-size:25px;line-height:34px;color:var(--white)}
.hero p{position:absolute;left:24px;top:146px;width:340px;font-family:'Arimo',sans-serif;font-size:11.5px;line-height:17px;color:#111}
.hero .btn{position:absolute;left:24px;top:202px;width:81px;height:31px;background:#f4f4f0;font-family:'Arimo',sans-serif;font-size:13px;line-height:31px;text-align:center;color:#222;border-radius:2px}
.services{position:absolute;left:150px;top:480px;width:704px;height:396px;border-top:3px double #3c3d3e;border-bottom:3px double #3c3d3e;background:linear-gradient(180deg,#1c1d1e 0%,var(--bg) 25%)}
.service{position:absolute;width:220px;text-align:center}
.icon{height:24px;display:flex;align-items:flex-end;justify-content:center}
.service h2{font-weight:300;font-size:17px;line-height:20px;color:var(--green-text);margin-top:6px}
.service p{font-size:8.3px;line-height:11.5px;color:var(--body-text);margin:6px auto 0;width:208px}
.more{display:block;width:42px;height:42px;margin:13px auto 0;border-radius:50%;background:#1b1c1c;border:1px solid #3c3d3e;font-size:9px;line-height:40px;color:#cfcfcf}
.welcome{position:absolute;left:157px;top:904px;width:385px}
.welcome h3,.videos h3{font-weight:300;font-size:15px;color:var(--green-text)}
.welcome p{font-size:8.8px;line-height:13.5px;color:var(--body-text);margin-top:14px}
.videos{position:absolute;left:577px;top:904px}
.video{position:relative;margin-top:14px;width:265px;height:149px;border:1px solid #555;background:linear-gradient(180deg,#8c9a6a 0%,#a07a5a 55%,#9a6e52 100%)}
.controls{position:absolute;left:6px;right:6px;bottom:6px;height:20px;background:rgba(20,20,20,.55)}
.footer{position:absolute;left:0;top:1122px;width:1004px;height:70px;background:var(--green)}
.footer-bottom{position:absolute;left:0;top:1192px;width:1004px;height:8px;background:#1b1c1d}
.footer-nav{position:absolute;left:158px;top:22px;display:flex;gap:17px;font-size:9px;color:var(--white)}
.copy{position:absolute;left:158px;top:40px;font-size:9px;color:var(--white)}
.social{position:absolute;left:726px;top:20px;display:flex;gap:13px}
.social span{width:30px;height:30px;border-radius:50%;background:#1c1d1d}
</style>
</head>
<body>
<div class="top-strip"></div>
<header class="header">
  <div class="brand"><span class="brand-dot"></span>Green Court Club</div>
  <div class="phones">
    <div><svg width="10" height="13" viewBox="0 0 10 13"><rect x="0.5" y="0.5" width="9" height="12" rx="1" fill="none" stroke="#fff"/><rect x="2" y="2" width="6" height="3" fill="#fff"/><rect x="2" y="7" width="6" height="4" fill="#fff" opacity=".7"/></svg>01 40 32 18 60</div>
    <div><svg width="10" height="13" viewBox="0 0 10 13"><rect x="0.5" y="0.5" width="9" height="12" rx="1" fill="none" stroke="#fff"/><rect x="2" y="2" width="6" height="3" fill="#fff"/><rect x="2" y="7" width="6" height="4" fill="#fff" opacity=".7"/></svg>54 62 09 37 11</div>
  </div>
  <div class="search">Enter Your Search
    <svg width="11" height="11" viewBox="0 0 11 11"><circle cx="4.5" cy="4.5" r="3.5" fill="none" stroke="#123e0d" stroke-width="1.5"/><line x1="7" y1="7" x2="10" y2="10" stroke="#123e0d" stroke-width="1.8"/></svg>
  </div>
</header>
<nav class="nav">
  <a class="active"><span>Home</span></a><a>About Us</a><a>Services</a><a>News</a><a>Coaches</a><a>Gallery</a><a>Contacts</a><a>Sport Store</a><a>Prices</a>
</nav>
<section class="hero" role="img" aria-label="Photo of a young player returning a ball on a clay tennis court, with other players behind the fence">
  <h1>Contrairementaune opinion répandue le Lorem Ipsum nest.</h1>
  <p>Le Lorem Ipsum est simplement du faux texte employé dans la composition et la mise en page avant impression. Le Lorem Ipsum est le faux texte standard de l'imprimerie depuis les années 1500.</p>
  <div class="btn">Read More</div>
</section>
<section class="services">
  <div class="service" style="left:9px;top:38px">
    <div class="icon"><svg width="20" height="20" viewBox="0 0 20 20"><circle cx="10" cy="10" r="9" fill="#2f9a24"/><path d="M4 4 Q10 10 16 16" stroke="#1c1d1e" stroke-width="1.5" fill="none"/></svg></div>
    <h2>TENNIS</h2><p>Le Lorem Ipsum est simplement du faux texte employé dans la composition et la mise en page avant impression Le Lorem Ipsum est le.</p><span class="more">MORE</span>
  </div>
  <div class="service" style="left:242px;top:38px">
    <div class="icon"><svg width="24" height="20" viewBox="0 0 24 20"><ellipse cx="11" cy="5" rx="5" ry="2.5" fill="#2f9a24"/><ellipse cx="10" cy="10" rx="7" ry="2.5" fill="#2f9a24"/><ellipse cx="11" cy="16" rx="9" ry="3" fill="#2f9a24"/></svg></div>
    <h2>SPA</h2><p>Le Lorem Ipsum est simplement du faux texte employé dans la composition et la mise en page avant impression Le Lorem Ipsum est le.</p><span class="more">MORE</span>
  </div>
  <div class="service" style="left:476px;top:38px">
    <div class="icon"><svg width="20" height="22" viewBox="0 0 20 22"><path d="M10 1 C16 1 19 5 18 11 C17 17 13 21 10 21 C7 21 3 17 2 11 C1 5 4 1 10 1Z" fill="#2f9a24"/></svg></div>
    <h2>BEAUTY CENTER</h2><p>Le Lorem Ipsum est simplement du faux texte employé dans la composition et la mise en page avant impression Le Lorem Ipsum est le.</p><span class="more">MORE</span>
  </div>
  <div class="service" style="left:9px;top:210px">
    <div class="icon"><svg width="24" height="20" viewBox="0 0 24 20"><path d="M12 1 L23 13 H1 Z" fill="#2f9a24"/><rect x="11" y="12" width="2" height="7" fill="#2f9a24"/></svg></div>
    <h2>FOREST</h2><p>Le Lorem Ipsum est simplement du faux texte employé dans la composition et la mise en page avant impression Le Lorem Ipsum est le.</p><span class="more">MORE</span>
  </div>
  <div class="service" style="left:242px;top:210px">
    <div class="icon"><svg width="24" height="20" viewBox="0 0 24 20"><path d="M3 3 L9 7 L16 6 L20 2 L22 5 L18 10 L20 18 L17 18 L15 12 L9 13 L6 18 L4 17 L6 11 Z" fill="#2f9a24"/></svg></div>
    <h2>HORSE RIDING</h2><p>Le Lorem Ipsum est simplement du faux texte employé dans la composition et la mise en page avant impression Le Lorem Ipsum est le.</p><span class="more">MORE</span>
  </div>
  <div class="service" style="left:476px;top:210px">
    <div class="icon"><svg width="16" height="24" viewBox="0 0 16 24"><circle cx="10" cy="3" r="2.5" fill="#2f9a24"/><path d="M9 6 L7 14 L8 23 M7 10 L2 5 M9 9 L14 2" stroke="#2f9a24" stroke-width="2.2" fill="none" stroke-linecap="round"/></svg></div>
    <h2>TRAINING</h2><p>Le Lorem Ipsum est simplement du faux texte employé dans la composition et la mise en page avant impression Le Lorem Ipsum est le.</p><span class="more">MORE</span>
  </div>
</section>
<section class="welcome">
  <h3>Welcome to Green Court Club</h3>
  <p>Le Lorem Ipsum est simplement du faux texte employé dans la composition et la mise en page avant impression. Le Lorem Ipsum est le faux texte standard de l'imprimerie depuis les années 1500, quand un peintre anonyme assembla ensemble des morceaux de texte pour réaliser un livre spécimen de polices de texte.</p>
  <p>Il n'a pas fait que survivre cinq siècles, mais s'est aussi adapté à la bureautique informatique, sans que son contenu n'en soit modifié. Il a été popularisé dans les années 1960.</p>
  <p>Grâce à la vente de feuilles Typoset contenant des passages du Lorem Ipsum, et, plus récemment, par son inclusion dans des applications de mise en page de texte, comme Mosaic PageBuilder.</p>
</section>
<section class="videos">
  <h3>Our Videos</h3>
  <div class="video" role="img" aria-label="Video still of three coaches standing on a clay court">
    <div class="controls">
      <svg width="253" height="20" viewBox="0 0 253 20"><rect x="2" y="1" width="22" height="18" fill="#2f9a24"/><path d="M10 5 L17 10 L10 15Z" fill="#fff"/><rect x="38" y="9" width="160" height="2" fill="#555"/><rect x="38" y="9" width="62" height="2" fill="#2f9a24"/><rect x="226" y="7" width="14" height="6" fill="#2f9a24" opacity=".8"/><rect x="244" y="7" width="5" height="5" fill="#ccc"/></svg>
    </div>
  </div>
</section>
<footer class="footer">
  <div class="footer-nav"><span>Home</span><span>About Us</span><span>Services</span><span>News</span><span>Coaches</span><span>Gallery</span><span>Contacts</span><span>Sport Store</span><span>Prices</span></div>
  <div class="copy">© Copyrights 2012 All rights Reserved</div>
  <div class="social"><span aria-label="Social link"></span><span aria-label="Social link"></span><span aria-label="Social link"></span></div>
</footer>
<div class="footer-bottom"></div>
</body>
</html>
```